Flyer for "Master the Mash Tun Basics" course

NEEDED: A6 flyer designed to advertise my first training course:
Intro to craft beer brewing

The company brand identity was recently bought from Pixel Harbor and it can be seen, with colour scheme on our website: www.TinmoorKettle.com.

The flyer is to be in line with my current brand identity and have a strong hook to push people to our site.

The flyer's goal is to get people to visit the site to book on a craft beer brewing training course. The info available to be included, although you have the freedom to include as much or as little as you see fit:

Currently a sale of 60% off on the course cost
RRP £120 Sale Price £50 (limited time only)
Courses will be run in central London
The website is TinmoorKettle.com
Hands on, half day course, brunch and a couple of sample beers included
Dates available:
14th December 2014
11th January 2015
18th January 2015
25th January 2015
1st February 2015
8th February 2015
15th February 2015
22nd February 2015

Logo file included, AI version available on request. Any photo on the TinmoorKettle.com site is available to be used. Simply pull of the site or I can send to you.

Colour scheme used on site: #FF9700 & #26210D

I will reply to any designs offered between 8pm and 11pm BST each day.

Good luch!

Hi everyone, We have now reviewed the first submissions and there are some ok, some good and a couple of great efforts in there. Here are the following common things that we commented on in our first reviews: 1. WHAT IS THE FLYER TRYING TO SAY... YOU'VE GOT 1 SECOND!!!! This flyer is to be given out in the street. That gives you 1second to tell the reader what the flyer is selling. That is the number 1 priority for the flyer. Please make it your priority as designers. 2. SALE SALE SALE This is the number 2 priority, people love SALES and a big colourful sticker saying SALE or 60% OFF (or both) is to be positioned so once the reader has seen that the flyer is about a craft beer brewing course, they see there is a sale on the course. 3. BRAND PERSONALITY 3rd priority is the Tinmoor Kettle brand identity. We picked this name, logo and colour scheme to stand out. Please use these to enhance points 1 & 2, but also get our logo on there is a bold and brash way. 4. USE THE BACK OF THE CARD Place any info that is not required in 1, 2 & 3 on the back, or even remove it all together if YOU feel it is not suited. You are the designer, so make some design decisions! We are happy to ask you to add things back in if we feel it is lacking. Our best guess (and we are NOT designers) is that putting either the dates OR a brief description of the course on the back would be enough info. If you think we can get bother, without overloading the page, give it a go! 5. CALL TO ACTION On the front and on the back, we want a CALL TO ACTION. Book at TinmoorKettle.com or just TinmoorKettle.com (you do not need http://www before it!!! We live in 2014 not 1994!!!) 6. MAKE IT BOLD, & THEN MAKE IT BOLDER This flyer is to stand out to a person that is handed 1 different leaflet every 2 minutes while walking down a busy London high street. We MUST stand out. Finally, thanks for all the designer so far, your efforts are greatly appreciated and we are very excited about the new revision of the design!

Target Market(s)

City living, young professionals who like to do fun things at the weekend.

Industry/Entity Type

Training

Font styles to use
Sans Serif

Colors
f78f20

Requirements
Must have
• Strong brand identity and call to action
In line with brand identity, see website www.TinmoorKettle.com

```html
<!DOCTYPE html>
<html lang="en">
<head>
<meta charset="utf-8">
<title>Intro to Craft Beer Brewing – Flyer</title>
<link rel="stylesheet" href="https://fonts.googleapis.com/css2?family=Archivo:wght@600;700;800&display=swap">
<style>
  :root {
    --page-bg: #ffffff;
    --brand-orange: #d98a26;
    --gold: #dc9a12;
    --ink-brown: #3d2414;
    --ink-brown-soft: #5a3a22;
    --logo-olive: #4a4220;
    --wood-light: #ece6e1;
    --wood-mid: #e0d8d1;
    --photo-dark: #121212;
    --photo-copper: #5a3a22;
    --white: #ffffff;
  }
  * { margin: 0; padding: 0; box-sizing: border-box; }
  html, body {
    width: 1200px; height: 1000px; overflow: hidden;
    background: var(--page-bg);
    font-family: "Archivo", "Helvetica Neue", Arial, sans-serif;
  }
  .flyer {
    position: absolute; left: 20px; top: 88px;
    width: 1160px; height: 825px; overflow: hidden;
    background: linear-gradient(90deg, var(--wood-light), var(--wood-mid) 50%, var(--wood-light));
  }
  .brand-column {
    position: absolute; left: 0; top: 0; width: 304px; height: 100%;
    background: var(--brand-orange);
  }
  .brand-name {
    position: absolute; left: 0; top: 120px; width: 304px;
    display: flex; flex-direction: column; align-items: center; gap: 18px;
    color: var(--logo-olive); font-weight: 800; font-size: 40px;
    text-transform: uppercase; letter-spacing: 1px; text-align: center; line-height: 1.05;
  }
  .brand-mark {
    width: 84px; height: 84px; border-radius: 50%; background: var(--logo-olive);
  }
  .brewhouse-art {
    position: absolute; left: 0; top: 520px; width: 561px; height: 305px;
    border-radius: 28px 28px 0 0;
    background: linear-gradient(180deg, var(--ink-brown-soft) 0%, var(--ink-brown) 100%);
  }
  .hero-band {
    position: absolute; left: 304px; top: 52px; width: 856px; height: 406px;
    background: radial-gradient(ellipse at 75% 45%, var(--photo-copper) 0%, #2a1d14 40%, var(--photo-dark) 75%);
  }
  .hero-text {
    position: absolute; left: 440px; top: 52px; width: 617px; height: 406px;
  }
  .rule {
    position: absolute; height: 2px; background: rgba(255,255,255,0.85);
  }
  .rule-top-left { top: 68px; left: 0; width: 212px; }
  .rule-top-right { top: 68px; left: 405px; width: 212px; }
  .rule-bottom { top: 323px; left: 0; width: 617px; }
  .intro {
    position: absolute; left: 0; top: 50px; width: 617px; text-align: center;
    color: var(--white); font-weight: 600; font-size: 38px; line-height: 1;
  }
  .title-top {
    position: absolute; left: -4px; top: 76px; width: 640px; white-space: nowrap;
    color: var(--gold); font-weight: 700; font-size: 132px; line-height: 1; letter-spacing: -3px;
  }
  .title-main {
    position: absolute; left: -4px; top: 190px; width: 640px; white-space: nowrap;
    color: var(--white); font-weight: 800; font-size: 122px; line-height: 1; letter-spacing: -1px;
  }
  .site-url {
    position: absolute; left: -20px; top: 338px; width: 657px; text-align: center; white-space: nowrap;
    color: var(--gold); font-weight: 700; font-size: 42px; letter-spacing: 2px; line-height: 1;
  }
  .sale {
    position: absolute; left: 700px; top: 530px; width: 400px; height: 250px;
    font-weight: 800; line-height: 1;
  }
  .sale-number {
    position: absolute; left: 0; top: 0; color: var(--ink-brown);
    font-size: 165px; letter-spacing: -6px;
  }
  .sale-percent {
    position: absolute; left: 192px; top: 2px; color: var(--gold); font-size: 74px;
  }
  .sale-off {
    position: absolute; left: 190px; top: 66px; color: var(--ink-brown); font-size: 92px; letter-spacing: -3px;
  }
  .sale-course {
    position: absolute; left: -4px; top: 140px; color: var(--gold); font-size: 106px; letter-spacing: -4px;
  }
</style>
</head>
<body>
  <main class="flyer">
    <aside class="brand-column">
      <div class="brand-name">
        <span class="brand-mark"></span>
        <span>Tinmoor<br>Kettle</span>
      </div>
    </aside>
    <div class="brewhouse-art" role="img" aria-label="Silhouette of brewing kettles, pipes and taps"></div>

    <div class="hero-band" role="img" aria-label="Close-up photo of copper beer taps in a dim bar"></div>
    <section class="hero-text">
      <div class="rule rule-top-left"></div>
      <div class="rule rule-top-right"></div>
      <p class="intro">Intro to</p>
      <h1 class="title-top">Craft Beer</h1>
      <h2 class="title-main">BREWING</h2>
      <div class="rule rule-bottom"></div>
      <p class="site-url">www.TinmoorKettle.com</p>
    </section>

    <section class="sale" aria-label="60% off course">
      <span class="sale-number">60</span>
      <span class="sale-percent">%</span>
      <span class="sale-off">off</span>
      <span class="sale-course">course</span>
    </section>
  </main>
</body>
</html>
```